Wix Commerce Site for Gas Fireplace & Heater Smartphone Controller

Our company 'tVarlo' makes and sells only 2 products (so far). A device that lets you control your gas fireplace or in-wall gas heater via bluetooth app on your smartphone.
We have a Wix site with a store that has our 2 products in it now, but would like a whole new design created specifically to market and sell these devices direct to consumer from our site. Existing site is gettvarlo.com
The only thing we are married to is the logo image, but everything else can be wiped clean. We have a few product images and some images/video of us as we built the prototypes and our own manufacturing process if incorporating them improves the sales pitch. Totally fine to leave it all out as well. We will need a gallery type page that we can add instructional video to of how to install the product and such once we get better videos produced. We are a family owned and operated business that has hand built every piece of this product ourselves from designing and assembling the electronics to coding the firmware and applications and even including 3D printing the cases for the initial production run (we are setting up our own injection mold system now to make future cases faster from locally recycled plastics.
We plan to stay on the Wix Pro plan so will need a site built that we can just drop in to our existing account.
The goal is to market 1 version as the "Gas Fireplace" controller and the other as the "In-Wall Gas Heater" controller.
I have included Screenshots from the Android and iOS apps that control the devices as well as a few other random pics that may or may not be useful, but let you see visually the types of devices they control so you can find better stock images to use as necessary. Also are a couple videos that are of low production value and will be remade more professionally soon as well.
I welcome any and all questions that will aid in design and will be as responsive as possible to design submissions.
links to our apps on the google play and apple store are nice to have somewhere as well.

```html
<!DOCTYPE html>
<html lang="en">
<head>
<meta charset="utf-8">
<title>tVarlo – Smart Gas Fireplace Control</title>
<link rel="stylesheet" href="https://fonts.googleapis.com/css2?family=Questrial&family=Lato:wght@300;400;700&display=swap">
<style>
:root{
  --navy:#17223b;
  --navy-deep:#131c33;
  --red:#b8383a;
  --orange:#d9843a;
  --gold:#d9b24a;
  --blue:#4a8fe6;
  --grey-bg:#e8e9ee;
  --grey-circle:#d3d4da;
  --ink:#1c1f2a;
  --body:#5b5f6b;
  --white:#ffffff;
}
*{box-sizing:border-box;margin:0;padding:0}
html,body{width:1200px;height:4335px;overflow:hidden}
body{position:relative;background:var(--white);font-family:'Lato',sans-serif;color:var(--ink)}
.abs{position:absolute}
h1,h2,.heading{font-family:'Questrial',sans-serif;font-weight:400}
.eyebrow{position:absolute;font-family:'Lato',sans-serif;font-size:12px;letter-spacing:9px;text-transform:uppercase}
.title{position:absolute;font-family:'Questrial',sans-serif;font-size:37px;line-height:1.25;text-transform:uppercase}
.rule{position:absolute;height:2px;width:86px}
.para{position:absolute;font-size:13.5px;line-height:25px;color:var(--body);font-weight:400}
.btn{position:absolute;display:flex;align-items:center;justify-content:center;border-radius:22px;font-size:11px;text-transform:uppercase;letter-spacing:.3px;font-family:'Lato',sans-serif}
.btn-solid{background:var(--blue);color:var(--white)}
.btn-ghost{border:1.5px solid var(--blue);color:var(--blue);background:var(--white)}
.photo{position:absolute}

/* header */
.site-header{position:absolute;left:0;top:0;width:1200px;height:120px}
.brand{position:absolute;display:flex;align-items:center;gap:10px;font-family:'Questrial',sans-serif;color:var(--white)}
.brand-dot{border-radius:50%;background:var(--orange)}
.nav{position:absolute;top:50px;left:0;width:1200px;font-size:14px;color:#c9cfdc}
.nav a{position:absolute;text-decoration:none;color:inherit}
.nav .active{color:var(--white);font-weight:700}
.nav .active::after{content:"";position:absolute;left:-3px;right:-3px;top:27px;height:2px;background:#c9cfdc}

/* hero */
.hero{position:absolute;left:0;top:0;width:1200px;height:665px;background:var(--navy)}
.hero h1{position:absolute;left:111px;top:222px;width:610px;font-size:42px;line-height:52px;color:var(--white)}

/* products */
.products{position:absolute;left:0;top:1365px;width:1200px;height:754px;background:linear-gradient(100deg,var(--red) 0%,var(--red) 48%,#c9603a 68%,var(--orange) 84%,var(--gold) 100%)}
.product-card{position:absolute;top:214px;width:284px;height:257px;border:1px solid rgba(255,255,255,.5)}
.product-name{position:absolute;top:492px;width:284px;text-align:center;color:#f6dcd4;font-size:15px}
.product-rule{position:absolute;top:526px;width:40px;height:1px;background:#f6dcd4}
.product-price{position:absolute;top:552px;width:284px;text-align:center;color:#f6e2dc;font-family:'Questrial',sans-serif;font-size:21px}

/* grey area */
.grey-area{position:absolute;left:0;top:2119px;width:1200px;height:1171px;background:var(--grey-bg)}

/* try it out */
.try{position:absolute;left:0;top:3290px;width:1200px;height:551px;background:linear-gradient(100deg,var(--red) 0%,var(--red) 55%,#cf6e3a 80%,var(--orange) 100%)}

/* footer */
.site-footer{position:absolute;left:0;top:4026px;width:1200px;height:309px;background:var(--navy-deep);color:#8d96ad}
.foot-links{position:absolute;font-size:12.5px;display:flex;gap:17px}
.subscribe{position:absolute;left:757px;top:117px;width:317px;height:53px;border-radius:27px;background:var(--white);display:flex;align-items:center;justify-content:space-between;padding:0 5px 0 22px}
.subscribe span{font-size:11px;color:#aab0bd}
.subscribe b{display:flex;align-items:center;justify-content:center;width:108px;height:42px;border-radius:21px;background:var(--blue);color:var(--white);font-size:11px;font-weight:400}
.social{position:absolute;top:262px;display:flex;align-items:center;gap:10px;font-size:12px}
.social i{display:flex;align-items:center;justify-content:center;width:30px;height:30px;border-radius:50%;background:#242e48}
</style>
</head>
<body>

<!-- HERO -->
<section class="hero">
  <svg class="abs" style="left:0;top:0" width="1200" height="665" viewBox="0 0 1200 665">
    <defs>
      <linearGradient id="heroWave" x1="0" y1="0" x2="1" y2="0">
        <stop offset="0" stop-color="#b8383a"/>
        <stop offset=".55" stop-color="#c54a3a"/>
        <stop offset=".8" stop-color="#d9843a"/>
        <stop offset="1" stop-color="#e09a3e"/>
      </linearGradient>
    </defs>
    <path d="M0,630 C260,560 520,610 760,520 C940,455 1080,420 1200,330 L1200,665 L0,665 Z" fill="url(#heroWave)"/>
    <path d="M0,665 L0,645 C320,575 760,585 1200,665 Z" fill="#ffffff"/>
  </svg>
  <h1>Control your gas fireplace or gas wall heater with your smart phone or device</h1>
  <div class="btn btn-solid" style="left:111px;top:454px;width:268px;height:54px;font-size:12px;gap:10px">Check out our product
    <svg width="20" height="12" viewBox="0 0 20 12"><path d="M1,6 H18 M13,1 L18,6 L13,11" stroke="#fff" stroke-width="1.6" fill="none"/></svg>
  </div>
  <div class="photo" role="img" aria-label="Smartphone showing the tVarlo app's Add a Device screen"
       style="left:791px;top:194px;width:240px;height:454px;border-radius:36px;background:linear-gradient(160deg,#1d2440 0%,#1d2440 45%,#b8383a 70%,#e09a3e 100%);transform:rotate(5deg);border:6px solid #2a2d36"></div>
</section>

<!-- HEADER -->
<header class="site-header">
  <div class="brand" style="left:72px;top:40px;font-size:29px"><span class="brand-dot" style="width:26px;height:26px"></span>tVarlo</div>
  <nav class="nav">
    <a class="active" style="left:546px">Home</a>
    <a style="left:628px">About Us</a>
    <a style="left:732px">Store</a>
    <a style="left:809px">Setup</a>
    <a style="left:889px">Testimonials</a>
    <a style="left:1012px">Contact</a>
    <svg class="abs" style="left:1106px;top:0" width="20" height="18" viewBox="0 0 20 18"><path d="M1,2 H4 L6,12 H16 L18,5 H5" stroke="#c9cfdc" stroke-width="1.5" fill="none"/><circle cx="7" cy="15.5" r="1.4" fill="#c9cfdc"/><circle cx="15" cy="15.5" r="1.4" fill="#c9cfdc"/></svg>
  </nav>
</header>

<!-- ABOUT -->
<section class="about">
  <svg class="abs" style="left:128px;top:772px" width="390" height="505" viewBox="0 0 390 505">
    <defs>
      <linearGradient id="arc" x1="0" y1="1" x2="1" y2="0">
        <stop offset="0" stop-color="#b8383a"/><stop offset=".6" stop-color="#c9603a"/><stop offset="1" stop-color="#d9b24a"/>
      </linearGradient>
    </defs>
    <path d="M320,4 A250,250 0 1,0 300,500 A240,240 0 1,1 320,4 Z" fill="url(#arc)"/>
  </svg>
  <div class="photo" role="img" aria-label="Photo of the two founders assembling controller prototypes at a table"
       style="left:168px;top:793px;width:460px;height:460px;border-radius:50%;background:radial-gradient(circle at 45% 55%,#8a7565 0%,#b9a995 55%,#d7cfc4 100%)"></div>
  <div class="eyebrow" style="left:686px;top:804px;color:var(--ink)">Who we are</div>
  <h2 class="title" style="left:680px;top:826px">About us</h2>
  <div class="rule" style="left:680px;top:883px;background:var(--ink)"></div>
  <p class="para" style="left:680px;top:926px;width:392px">After years in the gas fireplace industry, we had an idea. What if there was a way to control your gas fireplace or gas heating system with your smart phone? There are remotes out there that can do this, but who wants another remote control sitting on their coffee table!</p>
  <p class="para" style="left:680px;top:1072px;width:392px">It took us a few years, but we finally worked out the bugs. Our innovative technology allows you to bring your gas fireplace, or even your dated gas heating system, into the 21st century.</p>
  <div class="btn btn-ghost" style="left:680px;top:1204px;width:116px;height:42px">Learn more</div>
</section>

<!-- PRODUCTS -->
<section class="products">
  <div class="eyebrow" style="left:0;width:1200px;text-align:center;top:84px;color:#f0c9be">What we offer</div>
  <h2 class="title" style="left:0;width:1200px;text-align:center;top:108px;color:var(--white)">Our products</h2>
  <div class="rule" style="left:562px;top:164px;width:86px;background:#f0c9be"></div>

  <div class="product-card photo" role="img" aria-label="Black HearthSync fireplace controller box" style="left:305px;background:linear-gradient(160deg,#f2f2f2 0%,#d8d8d8 40%,#2b2b2e 60%,#e6e6e6 100%)"></div>
  <div class="product-name" style="left:305px">HearthSync - Gas Fireplaces</div>
  <div class="product-rule" style="left:427px"></div>
  <div class="product-price" style="left:305px">$119.00</div>

  <div class="product-card photo" role="img" aria-label="Open HearthSync wall heater controller cases" style="left:618px;background:linear-gradient(160deg,#9a8f85 0%,#4a4a4d 40%,#2c2c2f 65%,#8a8178 100%)"></div>
  <div class="product-name" style="left:618px">HearthSync - Gas Wall Heaters</div>
  <div class="product-rule" style="left:740px"></div>
  <div class="product-price" style="left:618px">$119.00</div>
</section>

<!-- HOW IT WORKS + SETUP (grey area) -->
<section class="grey-area">
  <div class="abs" style="left:576px;top:-141px;width:464px;height:464px;border-radius:50%;background:var(--grey-circle);clip-path:inset(141px 0 0 0)"></div>
  <div class="eyebrow" style="left:153px;top:94px;color:var(--ink)">What we do</div>
  <h2 class="title" style="left:153px;top:116px">How it works</h2>
  <div class="rule" style="left:153px;top:172px;background:var(--ink)"></div>
  <p class="para" style="left:153px;top:215px;width:395px">Lorem ipsum dolor sit amet, consectetur adipiscing elit, sed do eiusmod tempor incididunt ut labore et dolore magna aliqua. Ut enim ad minim veniam, quis nostrud exercitation ullamco laboris nisi ut aliquip ex ea commodo consequat. Duis aute irure dolor in reprehenderit in voluptate velit esse cillum dolore eu fugiat nulla pariatur.</p>
  <div class="btn btn-solid" style="left:153px;top:405px;width:116px;height:43px">Learn more</div>

  <div class="abs" role="img" aria-label="First app download badge" style="left:929px;top:459px;width:104px;height:32px;border:1.5px solid #9a9ca4;border-radius:5px;background:#f4f4f6"></div>
  <div class="abs" role="img" aria-label="Second app download badge" style="left:1047px;top:459px;width:104px;height:32px;border:1.5px solid #9a9ca4;border-radius:5px;background:#f4f4f6"></div>

  <div class="photo" role="img" aria-label="Video thumbnail: setting up the hardware" style="left:123px;top:619px;width:505px;height:391px;background:linear-gradient(180deg,#1f2a3d 0%,#253346 55%,#23302b 100%)"></div>
  <svg class="abs" style="left:342px;top:780px" width="70" height="70" viewBox="0 0 70 70"><circle cx="35" cy="35" r="35" fill="#fff"/><path d="M28,23 L49,35 L28,47 Z" fill="#17223b"/></svg>

  <h2 class="title" style="left:687px;top:627px;width:400px;line-height:47px">Setting up the hardware</h2>
  <div class="rule" style="left:687px;top:729px;background:var(--ink)"></div>
  <p class="para" style="left:687px;top:774px;width:395px">Lorem ipsum dolor sit amet, consectetur adipiscing elit, sed do eiusmod tempor incididunt ut labore et dolore magna aliqua. Ut enim ad minim veniam, quis nostrud exercitation ullamco laboris nisi ut aliquip ex ea commodo consequat. Duis aute irure dolor in reprehenderit in voluptate velit esse cillum dolore eu fugiat nulla pariatur.</p>
  <div class="btn btn-solid" style="left:687px;top:964px;width:116px;height:41px">Learn more</div>
</section>

<div class="photo" role="img" aria-label="Smartphone showing the tVarlo temperature control screen"
     style="left:660px;top:2030px;width:270px;height:520px;border-radius:38px;border:7px solid #d9c4bb;background:linear-gradient(165deg,#4a8fe6 0%,#4a8fe6 6%,#ffffff 7%,#ffffff 30%,#e9a392 50%,#d9843a 70%,#ffffff 85%);transform:rotate(3deg);box-shadow:10px 20px 30px rgba(0,0,0,.15)"></div>

<!-- TRY IT OUT -->
<section class="try">
  <div class="abs" style="left:111px;top:59px;width:44px;height:101px;background:rgba(255,255,255,.15)"></div>
  <h2 class="title" style="left:123px;top:84px;color:var(--white)">Try it out</h2>
  <div class="rule" style="left:123px;top:146px;background:#f0c9be"></div>
  <p class="para" style="left:123px;top:188px;width:395px;color:#f6dcd4">Lorem ipsum dolor sit amet, consectetur adipiscing elit, sed do eiusmod tempor incididunt ut labore et dolore magna aliqua. Ut enim ad minim veniam, quis nostrud exercitation ullamco laboris nisi ut aliquip ex ea commodo consequat. Duis aute irure dolor in reprehenderit in voluptate velit esse cillum dolore eu fugiat nulla pariatur.</p>
  <div class="btn btn-solid" style="left:123px;top:379px;width:106px;height:40px">Shop now</div>
</section>
<div class="photo" role="img" aria-label="Circuit boards laid out on a wooden floor" style="left:623px;top:3396px;width:212px;height:197px;border:2px solid #fff;background:linear-gradient(150deg,#7c6651,#4f7a63,#8a7258)"></div>
<div class="photo" role="img" aria-label="Person assembling controllers at a desk" style="left:623px;top:3615px;width:212px;height:284px;border:2px solid #fff;background:linear-gradient(160deg,#c9c2b6,#6d6a6e,#b9ad9c)"></div>
<div class="photo" role="img" aria-label="3D printer producing controller cases" style="left:858px;top:3396px;width:212px;height:285px;border:2px solid #fff;background:linear-gradient(160deg,#8a7a6a,#2a2c33,#a89686)"></div>
<div class="photo" role="img" aria-label="Bundles of blue wiring harnesses" style="left:858px;top:3703px;width:212px;height:196px;border:2px solid #fff;background:linear-gradient(150deg,#c9c3bb,#3f6f9a,#8a7f74)"></div>
<svg class="abs" style="left:586px;top:3640px" width="14" height="20" viewBox="0 0 14 20"><path d="M11,2 L3,10 L11,18" stroke="#fff" stroke-width="2" fill="none"/></svg>
<svg class="abs" style="left:1093px;top:3640px" width="14" height="20" viewBox="0 0 14 20"><path d="M3,2 L11,10 L3,18" stroke="#fff" stroke-width="2" fill="none"/></svg>

<!-- FOOTER -->
<footer class="site-footer">
  <div class="brand" style="left:126px;top:42px;font-size:40px"><span class="brand-dot" style="width:38px;height:38px"></span>tVarlo</div>
  <div class="foot-links" style="left:135px;top:126px"><span>About Us</span><span>Store</span><span>Setup</span><span>Testimonials</span><span>Contact</span></div>
  <div class="foot-links" style="left:135px;top:155px"><span>Terms &amp; Conditions</span><span>FAQs</span><span>Privacy Policy</span></div>
  <div class="heading abs" style="left:769px;top:58px;font-size:18px;color:var(--white)">GET IN TOUCH WITH US</div>
  <div class="abs" style="left:769px;top:96px;width:86px;height:1px;background:#8d96ad"></div>
  <div class="subscribe"><span>Enter your email</span><b>SUBSCRIBE</b></div>
  <div class="abs" style="left:96px;top:249px;width:1010px;height:1px;background:#28324b"></div>
  <div class="abs" style="left:131px;top:272px;font-size:11.5px">© 2023 by Ashgrove Studio Inc.</div>
  <div class="social" style="left:873px"><i><svg width="14" height="10" viewBox="0 0 14 10"><rect x=".5" y=".5" width="13" height="9" fill="none" stroke="#8d96ad"/><path d="M.5,.5 L7,6 L13.5,.5" fill="none" stroke="#8d96ad"/></svg></i>Email</div>
  <div class="social" style="left:971px"><i><svg width="10" height="10" viewBox="0 0 10 10"><circle cx="5" cy="5" r="4" fill="#8d96ad"/></svg></i>Community</div>
</footer>

</body>
</html>
```